Velvetorchid Hair & Beauty Business Card

Velvetorchid Hair & Beauty is a boutique salon located in the picturesque Lake Taupo NZ. The salon is very luxurious, opulent gold gilded mirrors, chandelier lit, contemporary french decor, sets the mood to create beautiful hair, makeup and all beauty services. Just had a new logo design and now after a new business card.
Logo
14 Korowhai Street
Taupo
Phone (07) 548 6193
www.velvetorchid.co.nz
email hair@velvetorchid.co.nz
Marlena Swithin
Also need a space to put in Stylist name, date, appointment time. thanks;)
Another idea is we could incorporate the wallpaper in the back ground either on the back or front or use an ornate glided frame (around the edge of the card) like on my website where my brides photos flash.
Decided against the wall paper but at least you can see our colour theme for the salon.
Updates

Please check out my updated brief . Thanks :)

Target Market(s)

25-60 years plus, mainly mid age females , wanting the best possible service , high standard of workmanship and money not a problem.

Industry/Entity Type

Boutique

Requirements
Must have
• Gold and silver

```html
<!DOCTYPE html>
<html lang="en">
<head>
<meta charset="utf-8">
<title>Velvetorchid Hair &amp; Beauty – Business Card</title>
<link rel="stylesheet" href="https://fonts.googleapis.com/css2?family=Quicksand:wght@400&family=Cormorant+Garamond:ital,wght@1,600;1,700&display=swap">
<style>
  :root {
    --page-bg: #ece8e1;
    --frame-dark: #3b3a1c;
    --frame-gold: #c9b24a;
    --frame-light: #efe08a;
    --panel-white: #ffffff;
    --brand-gold: #a8893a;
    --card-gold-light: #ddc98c;
    --card-gold: #cdb36c;
    --card-gold-deep: #b99c52;
    --ink-gold: #8a7232;
    --ink-faint: rgba(138, 114, 50, 0.35);
    --slit-grey: #9a9c9e;
  }
  * { box-sizing: border-box; margin: 0; padding: 0; }
  html, body {
    width: 1200px; height: 1000px; overflow: hidden;
    background: var(--page-bg);
  }
  .canvas { position: relative; width: 1200px; height: 1000px; }

  /* ---------- Front ---------- */
  .card-front {
    position: absolute; left: 260px; top: 60px;
    width: 680px; height: 400px;
    box-shadow: 0 6px 18px rgba(0,0,0,0.25);
  }
  .gilded-frame {
    position: absolute; inset: 0;
    background:
      linear-gradient(90deg, var(--frame-dark) 0 3%, transparent 3% 97%, var(--frame-dark) 97%),
      linear-gradient(180deg, var(--frame-dark) 0 5%, var(--frame-gold) 12%, var(--frame-light) 50%, var(--frame-gold) 88%, var(--frame-dark) 95%);
  }
  .front-panel {
    position: absolute; left: 62px; top: 56px; right: 62px; bottom: 56px;
    background: var(--panel-white);
    border-radius: 6px;
    box-shadow: inset 0 0 6px rgba(0,0,0,0.35);
    display: flex; flex-direction: column; align-items: center; justify-content: center;
  }
  .crest-ornament {
    width: 190px; height: 52px; margin-bottom: 10px;
    background: linear-gradient(180deg, #d9c47c, var(--brand-gold));
    border-radius: 40px 40px 8px 8px;
    opacity: 0.8;
  }
  .brand-name {
    font-family: "Quicksand", sans-serif; font-weight: 400;
    color: var(--brand-gold); text-align: center; line-height: 1.1;
  }
  .front-panel .brand-name { font-size: 46px; }
  .front-panel .brand-name span { display: block; font-size: 15px; letter-spacing: 2px; margin-top: 8px; }

  /* ---------- Back ---------- */
  .card-back {
    position: absolute; left: 260px; top: 520px;
    width: 680px; height: 400px;
    background: linear-gradient(135deg, var(--card-gold-light), var(--card-gold) 55%, var(--card-gold-deep));
    box-shadow: 0 6px 18px rgba(0,0,0,0.25);
    overflow: hidden;
  }
  .tab-strip {
    position: absolute; left: 0; top: 0; bottom: 0; width: 150px;
    border-right: 1px solid rgba(255,255,255,0.4);
  }
  .tab-slit {
    position: absolute; left: 138px; top: 210px; width: 12px; height: 190px;
    background: var(--slit-grey);
  }
  .tab-strip .brand-name {
    position: absolute; left: 75px; top: 200px;
    transform: translate(-50%, -50%) rotate(-90deg);
    white-space: nowrap; font-size: 30px;
  }
  .tab-strip .brand-name span { display: block; font-size: 10px; letter-spacing: 2px; margin-top: 4px; }
  .tab-ornament {
    position: absolute; left: 100px; top: 40px; width: 34px; height: 110px;
    background: linear-gradient(180deg, var(--ink-faint), rgba(138,114,50,0.15));
    border-radius: 16px;
  }
  .contact-block {
    position: absolute; left: 240px; top: 34px; width: 360px;
    text-align: center;
    font-family: "Cormorant Garamond", serif; font-style: italic; font-weight: 600;
    color: var(--ink-gold); font-size: 21px; line-height: 1.3;
    text-shadow: 0 1px 1px rgba(255,255,255,0.35);
  }
  .contact-block .contact-person { font-size: 28px; font-weight: 700; margin-top: 4px; }
  .contact-ornament {
    width: 150px; height: 30px; margin: 8px auto 0;
    background: linear-gradient(180deg, var(--ink-gold), rgba(138,114,50,0.5));
    border-radius: 14px; opacity: 0.7;
  }
  .appointment-clock { position: absolute; left: 470px; top: 200px; }
  .appointment-fields {
    position: absolute; left: 190px; top: 236px; width: 450px;
    font-family: "Cormorant Garamond", serif; font-style: italic; font-weight: 700;
    color: var(--ink-gold); font-size: 28px;
  }
  .field-row { position: relative; height: 48px; border-bottom: 5px solid var(--ink-gold); margin-bottom: 30px; }
  .field-row .field-label { position: absolute; left: 0; bottom: 2px; }
  .field-row .field-label.time { left: 250px; }
</style>
</head>
<body>
<main class="canvas">

  <section class="card-front" aria-label="Business card front">
    <div class="gilded-frame" role="img" aria-label="Ornate gilded picture frame border"></div>
    <div class="front-panel">
      <div class="crest-ornament" role="img" aria-label="Gold baroque scroll ornament"></div>
      <p class="brand-name">Velvetorchid<span>HAIR &amp; BEAUTY</span></p>
    </div>
  </section>

  <section class="card-back" aria-label="Business card back">
    <div class="tab-strip">
      <div class="tab-ornament" role="img" aria-label="Gold scroll ornament"></div>
      <p class="brand-name">Velvetorchid<span>HAIR &amp; BEAUTY</span></p>
    </div>
    <div class="tab-slit"></div>

    <div class="contact-block">
      <p>14 Korowhai Street, Taupo</p>
      <p>Phone: (07) 548 6193</p>
      <p>www.velvetorchid.co.nz</p>
      <p>email: hair@velvetorchid.co.nz</p>
      <p class="contact-person">Marlena Swithin</p>
      <div class="contact-ornament" role="img" aria-label="Gold scroll ornament"></div>
    </div>

    <svg class="appointment-clock" width="170" height="190" viewBox="0 0 170 190" aria-hidden="true">
      <g fill="none" stroke="rgba(240,225,170,0.7)" stroke-width="9" stroke-linecap="round">
        <circle cx="85" cy="100" r="62"/>
        <path d="M30 52 A30 30 0 0 1 62 28"/>
        <path d="M140 52 A30 30 0 0 0 108 28"/>
        <path d="M85 100 L85 62"/>
        <path d="M85 100 L115 112"/>
        <path d="M45 150 L32 172"/>
        <path d="M125 150 L138 172"/>
      </g>
    </svg>

    <div class="appointment-fields">
      <div class="field-row"><span class="field-label">stylist:</span></div>
      <div class="field-row"><span class="field-label">date:</span><span class="field-label time">time:</span></div>
    </div>
  </section>

</main>
</body>
</html>
```